WHOLE BLACK OLIVES (METAL CAN – 4950 ml / 2.5 kg NET WEIGHT)

1. Product:
Whole Black Olives
Black Olives

2. Packaging Specifications:
Container: Metal can

Capacity: 4950 ml

Net Weight: 2.5 kg

Label Type: directly printed on the can

Shape: Cylindrical industrial tin 50cmX24cm

3. Design Requirements:

Emphasize authenticity and quality (Mediterranean style

Modern yet clean design that stands out on wholesale shelves

Highlight product name clearly: “Whole Black Olives”

Include bilingual text (English / French Arabic if needed)

Space for barcode, nutritional table, ingredients, production/expiry date, net weight, drained weight

Brand: [LOMBA]

4. Front of Label Must Include:

Product name: Whole Black Olives

Net weight: 2.5 kg (4950 ml)

Drained weight: [to be confirmed]

imagery: olives, olive tree branches, Mediterranean field, etc.

Brand logo

5. Back of Label Must Include:
Ingredients:
Whole black olives, water, salt, ferrous gluconate (E579), citric acid
-The label must contain an image of black olives. big picture

Nutrition Facts Table (per 100 g):

Nutrient Amount
Energy 150 kcal
Fat 15 g
Saturated Fat 2 g
Carbohydrates 1 g
Sugars 0 g
Fiber 2.5 g
Protein 1.2 g
Salt 3.5 g

Additional Text (example):

Store in a cool, dry place.

Refrigerate after opening and consume within 7 days.

Target Market(s)

Targeting the Mediterranean and American markets.

Industry/Entity Type

agri-food industry

Font styles to use
Sans Serif
Decorative
Script

Colors
00AB8E
00BBA5
67D7C9
C6EFE9
E9F9F6
59FF00
82FF00
B8FF75
E3FFCB
F4FFEA
FFF300
FFF600
FEFA6F
FFFEC7
FFFEE8
FFC000
F8CF3A
FAE287
FDF2CF
FEFAEE
F0912C
F2A743
F7CA91
FBE8D2
FDF5EE
EB3D1F
EC4F4E
F09395
F8D3D4
FCEDEE

Requirements
Must have
• The design must include the logo and an image of black olives, name of product in English, freench and arabic, bar code
Nice to have
• The design must be unique and out of the box, incorporating the logo and a high-quality image of black olives. It should use eye-catching colors and create strong shelf appeal with an appetizing look and packaging that immediately captures consumer attention
Should not have
• "The design should be original and stand out, featuring the logo and a clear image of black olives. It must use appealing colors and a clean layout to attract attention while staying appetizing and uncluttered.

```html
<!DOCTYPE html>
<html lang="en">
<head>
<meta charset="utf-8">
<title>LOMBA Whole Black Olives – Can Label</title>
<link rel="stylesheet" href="https://fonts.googleapis.com/css2?family=Cinzel:wght@500;600&family=Montserrat:wght@400;500;600&family=Noto+Naskh+Arabic:wght@500&display=swap">
<style>
  :root {
    --backdrop: #ececec;
    --label-light: #f2f6dc;
    --label-mid: #e2ecc4;
    --label-edge: #d3e0ad;
    --navy: #26476b;
    --red: #e2463a;
    --ink: #2c2f2a;
    --olive-dark: #2b2f36;
    --olive-mid: #4a5160;
    --leaf: #6d9a3e;
    --code-zone: #fbfcf4;
  }
  * { box-sizing: border-box; margin: 0; padding: 0; }
  html, body { width: 1200px; height: 900px; overflow: hidden; }
  body {
    background: var(--backdrop);
    font-family: "Montserrat", sans-serif;
    color: var(--ink);
    display: flex;
    justify-content: center;
    align-items: center;
    gap: 60px;
  }
  .label-panel {
    width: 460px;
    height: 800px;
    background: linear-gradient(90deg, var(--label-edge) 0%, var(--label-light) 45%, var(--label-mid) 100%);
    display: flex;
    flex-direction: column;
    align-items: center;
    text-align: center;
    padding: 48px 36px 40px;
    position: relative;
  }
  .brand {
    display: flex;
    align-items: center;
    gap: 10px;
    font-family: "Cinzel", serif;
    font-weight: 600;
    font-size: 54px;
    color: var(--navy);
    letter-spacing: 2px;
  }
  .brand-dot {
    width: 16px; height: 16px;
    border-radius: 50%;
    background: var(--leaf);
  }
  .variant {
    font-family: "Cinzel", serif;
    font-weight: 600;
    color: var(--red);
    letter-spacing: 2px;
  }
  .name-en, .name-fr {
    font-family: "Cinzel", serif;
    font-weight: 600;
    color: var(--navy);
    line-height: 1.1;
  }
  .name-ar {
    font-family: "Noto Naskh Arabic", serif;
    font-weight: 500;
    color: var(--navy);
    direction: rtl;
  }
  /* Front */
  .front .variant { font-size: 40px; margin-top: 34px; }
  .front .name-en { font-size: 46px; margin-top: 14px; }
  .front .name-fr { font-size: 40px; margin-top: 10px; }
  .front .name-ar { font-size: 44px; margin-top: 8px; }
  .olive-art {
    width: 330px;
    height: 250px;
    margin-top: 22px;
    border-radius: 50%;
    background: radial-gradient(ellipse closest-side at 50% 55%, var(--olive-mid) 0%, var(--olive-dark) 50%, rgba(109,154,62,0.45) 80%, rgba(226,236,196,0) 100%);
  }
  .weights {
    margin-top: auto;
    font-size: 19px;
    line-height: 1.5;
  }
  /* Back */
  .back .variant { font-size: 26px; margin-top: 0; }
  .back .name-en { font-size: 32px; margin-top: 6px; }
  .back .name-fr { font-size: 27px; margin-top: 6px; }
  .back .name-ar { font-size: 30px; margin-top: 2px; }
  .ingredients { margin-top: 18px; font-size: 12px; line-height: 1.45; }
  .ingredients strong { display: block; font-weight: 600; font-size: 13px; }
  .nutrition {
    margin-top: 22px;
    width: 300px;
    border-collapse: collapse;
    border: 1px solid var(--ink);
    font-size: 12px;
  }
  .nutrition th, .nutrition td {
    padding: 3px 10px;
    border-left: 1px solid var(--ink);
    font-weight: 400;
    vertical-align: top;
  }
  .nutrition thead th { border-bottom: 1px solid var(--ink); padding: 6px 10px; font-weight: 500; }
  .nutrition th:first-child, .nutrition td:first-child { text-align: left; border-left: none; }
  .nutrition td:last-child, .nutrition th:last-child { text-align: center; }
  .nutrition tbody tr:first-child td { padding-top: 8px; }
  .nutrition tbody tr:last-child td { padding-bottom: 6px; }
  .about { margin-top: 26px; max-width: 330px; font-size: 12px; line-height: 1.5; color: #4a4d46; }
  .storage {
    margin-top: 22px;
    font-size: 12.5px;
    font-weight: 500;
    text-transform: uppercase;
    letter-spacing: 0.5px;
    line-height: 1.5;
  }
  .storage p + p { margin-top: 14px; }
  .barcode-zone {
    position: absolute;
    left: 14px;
    top: 470px;
    width: 30px;
    height: 220px;
    background: var(--code-zone);
    border: 1px solid rgba(44,47,42,0.25);
  }
</style>
</head>
<body>
  <section class="label-panel front">
    <div class="brand"><span class="brand-dot"></span>LOMBA</div>
    <p class="variant">WHOLE</p>
    <h1 class="name-en">BLACK OLIVES</h1>
    <p class="name-fr">OLIVES NOIRES</p>
    <p class="name-ar" lang="ar">زيتون أسود</p>
    <div class="olive-art" role="img" aria-label="Glossy whole black olives with green olive leaves"></div>
    <p class="weights">Net Wt. 2.5 kg (4950 ml)<br>Drained Wt. 0.0 kg (0000 ml)</p>
  </section>

  <section class="label-panel back">
    <div class="barcode-zone" role="img" aria-label="Space reserved for the product barcode"></div>
    <p class="variant">WHOLE</p>
    <h2 class="name-en">BLACK OLIVES</h2>
    <p class="name-fr">OLIVES NOIRES</p>
    <p class="name-ar" lang="ar">زيتون أسود</p>
    <p class="ingredients"><strong>Ingredients:</strong>Whole black olives, water, salt, ferrous<br>gluconate (E579), citric acid</p>
    <table class="nutrition">
      <thead>
        <tr><th>Nutritions</th><th>Typical Value<br>100g Approx.</th></tr>
      </thead>
      <tbody>
        <tr><td>Energy</td><td>150 kcal</td></tr>
        <tr><td>Fat</td><td>15 g</td></tr>
        <tr><td>Saturated Fat</td><td>2 g</td></tr>
        <tr><td>Carbohydrates</td><td>1 g</td></tr>
        <tr><td>Sugars</td><td>0 g</td></tr>
        <tr><td>Fiber</td><td>2.5 g</td></tr>
        <tr><td>Protein</td><td>1.2 g</td></tr>
        <tr><td>Salt</td><td>3.5 g</td></tr>
      </tbody>
    </table>
    <p class="about">Lorem ipsum dolor sit amet, consectetuer adipiscing elit, sed diam nonummy nibh euismod tincidunt ut laoreet dolore magna aliquam erat volutpat. Ut wisi enim ad minim veniam, quis nostrud exerci tation ullamcorper suscipit lobortis nisl ut aliquip ex ea commodo consequat.</p>
    <div class="storage">
      <p>Store in a cool, dry place.</p>
      <p>Refrigerate after opening and<br>consume within 7 days.</p>
    </div>
  </section>
</body>
</html>
```